Poster Design - Stand Up Paddle Eco Tour

We need a A3 size poster design (using Adobe Illustrator) for our company's stand up paddle tour. Our tour is on flat water, calm and safe, suitable for all ages and level.

WE provide worldclass SUP boards for our customers. And branded Joren Maltby life jacket. Our instructors are all well trained and exeprience. Plus they are super friendly. Every paddling trip come with a safety boat.

Please refer to attached files for text and photos.

Our website is www.brinkwaveoar.com.sg

IMPORTANT NOTE - The design has to be done in Adobe Illustrator. The winning designer has to submit the working file in Adobe Illustrator.

Target Market(s)

Working adult - 20 - 35 year old

Industry/Entity Type

Tourism

Requirements
Must have
• The project MUST be done in Adobe Illustrator and the winning designer has to submit the artwork to us in Adobe Illustrator format.
Nice to have
• pleasant to look at.

```html
<!DOCTYPE html>
<html lang="en">
<head>
<meta charset="utf-8">
<title>Brinkwave Oar – SUP Eco Tour Poster</title>
<link href="https://fonts.googleapis.com/css2?family=Open+Sans:wght@400;600;800&display=swap" rel="stylesheet">
<style>
  :root {
    --grad-top: #b46fc6;
    --grad-upper: #9a86d6;
    --grad-mid: #52b9d8;
    --grad-low: #2fc3b8;
    --grad-bottom: #3cc78a;
    --ink: #ffffff;
    --navy: #1d2a44;
    --photo-a: #5e9fb8;
    --photo-b: #7aa56a;
    --photo-c: #c9d6dc;
  }
  * { margin: 0; padding: 0; box-sizing: border-box; }
  html, body { width: 849px; height: 1200px; overflow: hidden; }
  body { font-family: "Open Sans", Arial, sans-serif; color: var(--ink); }
  .poster {
    position: relative;
    width: 849px;
    height: 1200px;
    overflow: hidden;
    background: linear-gradient(180deg, var(--grad-top) 0%, var(--grad-upper) 22%, var(--grad-mid) 48%, var(--grad-low) 72%, var(--grad-bottom) 100%);
  }
  .brand {
    position: absolute;
    top: 40px; left: 0; width: 100%;
    text-align: center;
  }
  .brand-name {
    display: inline-block;
    background: var(--navy);
    color: var(--ink);
    font-weight: 800;
    font-size: 28px;
    letter-spacing: 3px;
    text-transform: uppercase;
    padding: 34px 30px 40px;
    border-radius: 6px;
  }
  .headline {
    position: absolute;
    top: 412px; left: 70px; width: 709px;
    text-align: center;
    font-weight: 800;
    font-size: 27px;
    line-height: 1.32;
    text-shadow: 0 1px 3px rgba(40, 40, 90, .45);
  }
  .intro {
    position: absolute;
    left: 90px; width: 669px;
    text-align: center;
    font-size: 18.5px;
    line-height: 1.42;
  }
  .intro-levels { top: 575px; }
  .intro-group { top: 705px; }
  .contact {
    position: absolute;
    top: 835px; left: 60px;
    font-size: 15px;
    line-height: 1.5;
  }
  .contact p + p.gap { margin-top: 14px; }
  .gallery { position: absolute; left: 0; top: 985px; width: 849px; height: 180px; }
  .photo {
    position: absolute;
    border: 4px solid #fff;
    box-shadow: 0 2px 6px rgba(0,0,0,.25);
  }
  .photo-1 { left: 22px;  top: 0;    width: 170px; height: 168px; background: linear-gradient(180deg, var(--photo-c), var(--photo-b) 60%, var(--photo-a)); }
  .photo-2 { left: 178px; top: 8px;  width: 162px; height: 128px; background: linear-gradient(180deg, #9fc4dd, var(--photo-a)); }
  .photo-3 { left: 335px; top: 12px; width: 170px; height: 118px; background: linear-gradient(180deg, #b7d0de, var(--photo-b) 45%, var(--photo-a)); }
  .photo-4 { left: 498px; top: 6px;  width: 170px; height: 134px; background: linear-gradient(180deg, #a9c9dc, var(--photo-b) 40%, #4d8fa8); }
  .photo-5 { left: 665px; top: 0;    width: 165px; height: 165px; background: linear-gradient(180deg, #d4e0e6, var(--photo-b) 55%, var(--photo-a)); }
</style>
</head>
<body>
<main class="poster">
  <header class="brand">
    <span class="brand-name">Brinkwave Oar</span>
  </header>

  <h1 class="headline">Explore the natural coastal surroundings and waterways of Johor on a SUP adventure touring board</h1>

  <p class="intro intro-levels">Our tours are flat-water and appropriate for all ages and levels.<br>We have the best possible service and equipment.<br>Join us for a fun and relaxing day.</p>

  <p class="intro intro-group">What could be better than a group guided tour?<br>With life vests and a safety boat for our guided tour,<br>you can be assured of a secured environment<br>while you focus on just having fun and creating life's<br>best memories with friends and family.</p>

  <section class="contact">
    <p>Timing: Morning, afternoon, and sunset session</p>
    <p>Location: Sendang River, set off from Teluk Meranti, Pantai Biru (next to Pasir Lembut)</p>
    <p class="gap">Contact us for booking. We do not accept walk-in.</p>
    <p>www.brinkwaveoar.com.sg</p>
    <p>Facebook: Brinkwave Oar</p>
    <p>Booking Contact: booking@brinkwaveoar.com.sg</p>
  </section>

  <div class="gallery">
    <div class="photo photo-1" role="img" aria-label="Mangrove shoreline with paddlers on calm water"></div>
    <div class="photo photo-2" role="img" aria-label="Group of stand up paddlers on open water"></div>
    <div class="photo photo-3" role="img" aria-label="Paddlers lined up on boards near the river bank"></div>
    <div class="photo photo-4" role="img" aria-label="Paddler on a yellow board along the mangroves"></div>
    <div class="photo photo-5" role="img" aria-label="Paddlers heading down a tree-lined waterway"></div>
  </div>
</main>
</body>
</html>
```